Tarrow Building Ventures needs a Business card design and logo

We Need a business card design and logo for a Building & Construction business based in Melbourne. We work in both the Domestic & Commercial sector. We specialize in all aspects of building including extensions, Renovations, and alterations. Construction Management, Project Management, And labour hire
Updates

Industry/Entity Type

Business

```html
<!DOCTYPE html>
<html lang="en">
<head>
<meta charset="utf-8">
<title>Tarrow Building Ventures – Business Card</title>
<link rel="stylesheet" href="https://fonts.googleapis.com/css2?family=Arimo:wght@400;700&display=swap">
<style>
  :root {
    --stage: #2b2b2b;
    --card: #f1f1f1;
    --card-shade: #e4e4e4;
    --facet: #d9d9d9;
    --ink: #262626;
    --ink-soft: #4a4a4a;
    --accent: #e5232a;
  }
  * { box-sizing: border-box; margin: 0; padding: 0; }
  html, body {
    width: 1200px; height: 900px; overflow: hidden;
    background: var(--stage);
    font-family: "Arimo", Arial, sans-serif;
  }
  .stage {
    width: 1200px; height: 900px;
    display: flex; flex-direction: column;
    align-items: center; justify-content: center; gap: 44px;
  }
  .card {
    position: relative;
    width: 660px; height: 377px;
    border-radius: 26px;
    background: var(--card);
    overflow: hidden;
    color: var(--ink);
  }
  .card-facets { position: absolute; inset: 0; }

  /* Front face */
  .brand {
    position: absolute; left: 52px; top: 62px;
    display: flex; align-items: center; gap: 12px;
  }
  .brand-square { width: 30px; height: 30px; background: var(--ink); }
  .brand-name {
    font-weight: 700; font-size: 24px; letter-spacing: 0.3px;
    color: var(--ink); text-transform: uppercase;
  }
  .holder {
    position: absolute; left: 52px; top: 214px;
  }
  .holder-name { font-size: 27px; font-weight: 700; color: var(--ink); }
  .holder-name .surname { color: var(--accent); font-weight: 400; }
  .contact { list-style: none; margin-top: 14px; font-size: 15px; line-height: 20px; color: var(--ink-soft); }
  .contact .label { color: var(--accent); }
  .services {
    position: absolute; right: 44px; top: 150px;
    font-size: 15px; line-height: 19px; color: var(--ink-soft);
  }
  .services .label { color: var(--accent); }

  /* Back face */
  .card-back .structure-photo {
    position: absolute; inset: 0;
    background: linear-gradient(120deg, #f4f4f4 0%, #ececec 45%, #dedede 70%, #e9e9e9 100%);
  }
  .back-content {
    position: absolute; inset: 0;
    display: flex; flex-direction: column; align-items: center; justify-content: center;
    text-align: center;
  }
  .back-brand { display: flex; align-items: center; gap: 14px; }
  .back-brand .brand-square { width: 38px; height: 38px; }
  .back-brand .brand-name { font-size: 34px; }
  .tagline { margin-top: 8px; font-size: 19px; color: var(--ink); }
  .website { margin-top: 34px; font-size: 17px; color: var(--accent); }
</style>
</head>
<body>
<main class="stage">

  <section class="card card-front" aria-label="Business card front">
    <svg class="card-facets" width="660" height="377" viewBox="0 0 660 377" aria-hidden="true">
      <polygon points="300,0 660,0 660,120 460,377 250,377" fill="var(--card-shade)" opacity="0.6"/>
      <polygon points="420,0 660,0 660,70" fill="var(--facet)" opacity="0.5"/>
      <polygon points="250,377 360,180 460,377" fill="var(--facet)" opacity="0.35"/>
    </svg>

    <div class="brand">
      <span class="brand-square"></span>
      <span class="brand-name">Tarrow Building Ventures</span>
    </div>

    <div class="holder">
      <h1 class="holder-name">Dean <span class="surname">Tarrow</span></h1>
      <ul class="contact">
        <li><span class="label">mobile:</span> 0400 555 218</li>
        <li><span class="label">office:</span> (03) 9000 4417</li>
        <li><span class="label">email:</span> info@tarrowbuildingventures.com</li>
      </ul>
    </div>

    <div class="services">
      <p class="label">Service:</p>
      <p>Extentions - Renovations</p>
      <p>Alterations - Decks - Pargolas</p>
    </div>
  </section>

  <section class="card card-back" aria-label="Business card back">
    <div class="structure-photo" role="img" aria-label="Faint photograph of a building frame under construction"></div>
    <div class="back-content">
      <div class="back-brand">
        <span class="brand-square"></span>
        <span class="brand-name">Tarrow Building Ventures</span>
      </div>
      <p class="tagline">Domestic &amp; Commercial Builders</p>
      <p class="website">www.tarrowbuildingventures.com</p>
    </div>
  </section>

</main>
</body>
</html>
```